Vorbly BIZ Card, email signature & Stationary

Professional business cards, email signatures and ms word letterhead

Target Market(s)

business owners

Industry/Entity Type

cloud hosting

Contact Information for Business Card

name title office phone number , direct line, fax email address web site

Font styles to use
Other font styles liked:
• something that compliments font in logo

```html
<!DOCTYPE html>
<html lang="en">
<head>
<meta charset="utf-8">
<title>Vorbly Business Card</title>
<link href="https://fonts.googleapis.com/css2?family=Jost:wght@400;500&display=swap" rel="stylesheet">
<style>
  :root {
    --backdrop: #5a5a5a;
    --card-dark: #2e2e2e;
    --card-light: #ffffff;
    --brand-red: #e8262c;
    --text-light: #f2f2f2;
    --watermark-grey: #3a3a3a;
  }
  * { box-sizing: border-box; margin: 0; padding: 0; }
  html, body {
    width: 1200px;
    height: 1200px;
    overflow: hidden;
    background: var(--backdrop);
    font-family: "Jost", "Futura", sans-serif;
  }
  .canvas {
    position: relative;
    width: 1200px;
    height: 1200px;
  }
  .card {
    position: absolute;
    width: 690px;
    height: 395px;
    overflow: hidden;
  }
  .card--front {
    left: 266px;
    top: 158px;
    background: var(--card-dark);
  }
  .card--back {
    left: 262px;
    top: 652px;
    background: var(--card-light);
    display: flex;
    align-items: center;
    justify-content: center;
  }
  .wordmark {
    color: var(--brand-red);
    font-weight: 400;
    line-height: 1;
    letter-spacing: -1px;
  }
  .card--front .wordmark {
    position: absolute;
    left: 42px;
    top: 34px;
    font-size: 78px;
  }
  .card--back .wordmark {
    font-size: 150px;
    margin-top: -6px;
  }
  .holder {
    position: absolute;
    left: 43px;
    top: 170px;
  }
  .holder__name {
    color: var(--brand-red);
    font-size: 26px;
    font-weight: 400;
    letter-spacing: -0.8px;
    line-height: 1.1;
  }
  .holder__title {
    color: var(--text-light);
    font-size: 17px;
    margin-top: 5px;
  }
  .contact-list {
    position: absolute;
    left: 44px;
    top: 256px;
    list-style: none;
  }
  .contact-list__item {
    display: flex;
    align-items: center;
    height: 21px;
    color: var(--text-light);
    font-size: 17px;
  }
  .contact-list__icon {
    width: 13px;
    height: 13px;
    margin-right: 12px;
    fill: var(--brand-red);
    flex: none;
  }
  .watermark-name {
    position: absolute;
    left: 360px;
    top: 140px;
    color: var(--watermark-grey);
    font-size: 108px;
    font-weight: 400;
    line-height: 1;
    letter-spacing: -1px;
  }
</style>
</head>
<body>
<div class="canvas">

  <section class="card card--front">
    <div class="wordmark">Vorbly</div>

    <div class="holder">
      <div class="holder__name">DANA MERROW</div>
      <div class="holder__title">President</div>
    </div>

    <ul class="contact-list">
      <li class="contact-list__item">
        <svg class="contact-list__icon" viewBox="0 0 16 16"><path d="M3 1l3 3-1.5 2c1 2 2.5 3.5 4.5 4.5L11 9l3 3-2 3C6 14 2 10 1 3z"/></svg>
        555-210-4817
      </li>
      <li class="contact-list__item">
        <svg class="contact-list__icon" viewBox="0 0 16 16"><path d="M4 0h8v16H4zM5.5 2v10h5V2zM7 13.5h2v1H7z" fill-rule="evenodd"/></svg>
        555-210-4892
      </li>
      <li class="contact-list__item">
        <svg class="contact-list__icon" viewBox="0 0 16 16"><path d="M4 1h8v4H4zM1 6h14v6h-2v-2H3v2H1zM4 11h8v4H4z"/></svg>
        555-210-4830
      </li>
      <li class="contact-list__item">
        <svg class="contact-list__icon" viewBox="0 0 16 16"><path d="M0 3h16v10H0z"/><path d="M1 4l7 5 7-5" stroke="#2e2e2e" stroke-width="1.3" fill="none"/></svg>
        hello@vorbly.com
      </li>
      <li class="contact-list__item">
        <svg class="contact-list__icon" viewBox="0 0 16 16"><circle cx="8" cy="8" r="7.5"/><path d="M4 4c2 0 2 2 4 2s1 3-1 3-1 3-3 2M11 3c-1 2 1 3 2 4" stroke="#2e2e2e" stroke-width="1.2" fill="none"/></svg>
        www.vorbly.com
      </li>
    </ul>

    <div class="watermark-name" aria-hidden="true">Vorbly</div>
  </section>

  <section class="card card--back">
    <div class="wordmark">Vorbly</div>
  </section>

</div>
</body>
</html>
```